Bright Harbor Business Cards & Stationary
Bright Harbor
Bright Harbor Business Cards & Stationary -
Creative Brief
Professional
Dana Verick
4417 Wexmoor Lane Bozeman, MT 59263
dana@brightharborfunds.example
www.brightharborfunds.example
I have two companies, Bright Harbor Wealth Management, LLC and Bright Harbor Realty Advisors, LLC. I use the same logo for both companies with a different tagline and color for each company. I will use one business card for both companies with one company on one side of the card and the other company on the other side of the card. Other than the colors, the business cards and stationary will have the same design.
Bright Harbor Realty Advisors logo Dana Verick 4417 Wexmoor Lane Bozeman, MT 59263 406-739-4802 dana@brightharborestates.example www.brightharborestates.example

```html
<!DOCTYPE html>
<html lang="en">
<head>
<meta charset="utf-8">
<title>Bright Harbor Stationery Set</title>
<link href="https://fonts.googleapis.com/css2?family=Lato:wght@400;700&display=swap" rel="stylesheet">
<style>
:root{
  --board:#8f8f8f;
  --paper:#ffffff;
  --wealth:#2f5f78;
  --realty:#6a4a2f;
  --ink:#555555;
  --caption:#d8d8d8;
  --fold:#dcdcdc;
}
*{box-sizing:border-box;margin:0;padding:0}
html,body{width:1200px;height:362px;overflow:hidden}
body{background:var(--board);position:relative;font-family:"Lato",sans-serif}
.sheet{position:absolute;background:var(--paper);box-shadow:0 1px 3px rgba(0,0,0,.35)}
.brand{position:absolute;white-space:nowrap;line-height:1}
.brand-name{display:block;font-family:"Lato",sans-serif;font-weight:700;font-size:8px;color:var(--wealth)}
.brand-line{display:block;margin-top:2px;font-size:3.6px;color:var(--ink);letter-spacing:.3px}
.realty .brand-name{color:var(--realty)}
.contact{position:absolute;font-size:3.4px;line-height:5px;color:var(--ink);white-space:nowrap}
.caption{position:absolute;font-size:4px;color:var(--caption);white-space:nowrap}
.base-band{position:absolute;left:0;right:0;bottom:0;height:7px;background:linear-gradient(90deg,var(--realty),#8a6a48,var(--realty))}
.flap{position:absolute;inset:0}
.back-name{position:absolute;left:0;right:0;text-align:center;font-weight:700;font-size:6px;color:var(--wealth);white-space:nowrap}
.realty .back-name{color:var(--realty)}
</style>
</head>
<body>

<p class="caption" style="left:14px;top:152px">Business cards</p>
<section class="sheet card" style="left:14px;top:161px;width:101px;height:57px">
  <div class="brand" style="left:8px;top:8px"><span class="brand-name">Bright Harbor</span><span class="brand-line">Wealth Management</span></div>
  <p class="contact" style="left:8px;top:29px">Dana Verick<br>4417 Wexmoor Lane Bozeman, MT 59263<br>406-739-4802<br>dana@brightharborfunds.example</p>
</section>
<section class="sheet card realty" style="left:14px;top:227px;width:101px;height:55px">
  <div class="brand" style="left:8px;top:8px"><span class="brand-name">Bright Harbor</span><span class="brand-line">Realty Advisors</span></div>
  <p class="contact" style="left:8px;top:27px">Dana Verick<br>4417 Wexmoor Lane Bozeman, MT 59263<br>406-739-4802<br>dana@brightharborestates.example</p>
</section>

<section class="sheet letterhead" style="left:144px;top:11px;width:216px;height:283px">
  <div class="brand" style="left:14px;top:14px"><span class="brand-name">Bright Harbor</span><span class="brand-line">Wealth Management</span></div>
  <p class="contact" style="left:14px;top:252px">4417 Wexmoor Lane<br>Bozeman, MT 59263<br>406-739-4802<br>www.brightharborfunds.example</p>
</section>
<p class="caption" style="left:144px;top:298px">Letterhead</p>

<section class="sheet letterhead realty" style="left:377px;top:11px;width:223px;height:294px">
  <div class="brand" style="left:14px;top:14px"><span class="brand-name">Bright Harbor</span><span class="brand-line">Realty Advisors</span></div>
  <p class="contact" style="left:14px;top:258px">4417 Wexmoor Lane<br>Bozeman, MT 59263<br>406-739-4802<br>www.brightharborestates.example</p>
  <div class="base-band"></div>
</section>
<p class="caption" style="left:377px;top:309px">Letterhead</p>

<section class="sheet envelope" style="left:624px;top:55px;width:204px;height:109px">
  <div class="brand" style="left:10px;top:10px"><span class="brand-name">Bright Harbor</span><span class="brand-line">Wealth Management</span></div>
</section>
<p class="caption" style="left:700px;top:168px">Envelope front</p>
<section class="sheet envelope realty" style="left:624px;top:185px;width:204px;height:111px">
  <div class="brand" style="left:10px;top:10px"><span class="brand-name">Bright Harbor</span><span class="brand-line">Realty Advisors</span></div>
</section>
<p class="caption" style="left:700px;top:300px">Envelope front</p>

<section class="sheet envelope-back" style="left:888px;top:55px;width:204px;height:109px">
  <svg class="flap" viewBox="0 0 204 109" preserveAspectRatio="none"><path d="M0 0 L102 48 L204 0 M0 109 L82 58 M204 109 L122 58" fill="none" stroke="var(--fold)" stroke-width="1"/></svg>
  <span class="back-name" style="top:36px">Bright Harbor</span>
</section>
<p class="caption" style="left:965px;top:168px">Envelope back</p>
<section class="sheet envelope-back realty" style="left:888px;top:185px;width:204px;height:111px">
  <svg class="flap" viewBox="0 0 204 111" preserveAspectRatio="none"><path d="M0 0 L102 49 L204 0 M0 111 L82 59 M204 111 L122 59" fill="none" stroke="var(--fold)" stroke-width="1"/></svg>
  <span class="back-name" style="top:37px">Bright Harbor</span>
</section>
<p class="caption" style="left:965px;top:300px">Envelope back</p>

</body>
</html>
```